Classic Minimalistic Business Card

Design a classic, minimalistic Business Card. Please find inspiration in the attached Classic Minimalistic examples. My information:
Name: Glen Ovamir
Company: Ovamir Capital
Logo: OC
Address: 1470 N Thornwick Rd, Suite 210 | Larkfield, IL 60198
Phone: 630-555-0192
Email: glenovamir@pvt.insure
Slogan: Building Strength Through Capital

Feel free to leave out any of the information above except my name.

I have selected Double-sided, but I am also open to Single-sided

Target Market(s)

22-70. income greater than 150k/year

Industry/Entity Type

Finance

Contact Information for Business Card

See Project Description

Requirements
Must have
• Ivory or "antiqued" background similar to the reference pictures

```html
<!DOCTYPE html>
<html lang="en">
<head>
<meta charset="utf-8">
<title>Ovamir Capital – Business Card</title>
<link href="https://fonts.googleapis.com/css2?family=Gelasio:wght@400&family=Cutive+Mono&family=Courier+Prime:wght@700&family=Jost:wght@500&display=swap" rel="stylesheet">
<style>
  :root {
    --backdrop: #1c1c1c;
    --card-ivory: #cdbd9f;
    --card-light: #d6c8ad;
    --card-shade: #c2b08f;
    --ink: #1e1e1e;
  }
  html, body {
    margin: 0;
    padding: 0;
    width: 1200px;
    height: 1200px;
    overflow: hidden;
    background: var(--backdrop);
  }
  .sheet {
    position: relative;
    width: 1200px;
    height: 1200px;
    display: flex;
    align-items: center;
    justify-content: center;
    gap: 40px;
  }
  .card {
    position: relative;
    width: 540px;
    height: 308px;
    background:
      radial-gradient(ellipse at 30% 20%, var(--card-light) 0%, transparent 60%),
      radial-gradient(ellipse at 80% 85%, var(--card-shade) 0%, transparent 55%),
      var(--card-ivory);
    color: var(--ink);
    box-sizing: border-box;
  }
  /* Front face */
  .card--front {
    display: flex;
    flex-direction: column;
    align-items: center;
    justify-content: center;
  }
  .brand-dot {
    width: 60px;
    height: 60px;
    border-radius: 50%;
    background: var(--ink);
    margin-bottom: 22px;
  }
  .brand-rule {
    display: block;
    width: 276px;
    height: 4px;
    margin-bottom: 10px;
  }
  .brand-name {
    font-family: "Gelasio", serif;
    font-weight: 400;
    font-size: 21px;
    letter-spacing: 1.5px;
    text-transform: uppercase;
    margin: 0;
    line-height: 1.1;
  }
  .brand-slogan {
    font-family: "Jost", sans-serif;
    font-weight: 500;
    font-size: 8px;
    letter-spacing: 4px;
    text-transform: uppercase;
    margin: 10px 0 0;
  }
  /* Back face */
  .card--back {
    text-align: center;
    padding-top: 98px;
  }
  .person-name {
    font-family: "Gelasio", serif;
    font-size: 41px;
    font-weight: 400;
    margin: 0;
    line-height: 1;
  }
  .address {
    font-family: "Cutive Mono", monospace;
    font-size: 15px;
    line-height: 27px;
    color: var(--ink);
    margin: 14px 0 0;
  }
  .contact-row {
    position: absolute;
    left: 26px;
    right: 26px;
    bottom: 14px;
    display: flex;
    justify-content: space-between;
    align-items: baseline;
  }
  .phone {
    font-family: "Cutive Mono", monospace;
    font-size: 17px;
  }
  .email {
    font-family: "Courier Prime", monospace;
    font-weight: 700;
    font-size: 15px;
  }
</style>
</head>
<body>
  <main class="sheet">
    <section class="card card--front" aria-label="Business card front">
      <div class="brand-dot"></div>
      <svg class="brand-rule" viewBox="0 0 276 4" aria-hidden="true">
        <path d="M0 2 Q138 0.6 276 2 Q138 3.2 0 2 Z" fill="#1e1e1e"/>
      </svg>
      <h1 class="brand-name">Ovamir Capital</h1>
      <p class="brand-slogan">Building Strength Through Capital</p>
    </section>

    <section class="card card--back" aria-label="Business card back">
      <h2 class="person-name">Glen Ovamir</h2>
      <p class="address">1470 N Thornwick Rd, Suite 210<br>Larkfield, IL 60198</p>
      <div class="contact-row">
        <span class="phone">630-555-0192</span>
        <span class="email">glenovamir@pvt.insure</span>
      </div>
    </section>
  </main>
</body>
</html>
```